Vordaline - Fitness Coach. Needs a Business Card Design that I can also use for other advertising

Established 2012, I have finished the KTRB National Certificate in Fitness & Personal Training. Harlow Cross First Aid Certificate. I have the Auckland 800m track records for MW45. I also came 1st at the 2012 Pellamar Games in 800 & 1500m. I am passionate about health & fitness and would like to help people reach their health & fitness goals. I also take health & fitness weekends. Main interests - Running, Weight Training, Yoga & Aqua Jogging. I like strength/power, but am femine.

Target Market(s)

Male or Female 18 and over that wants to improve their health & fitness

Industry/Entity Type

Advertising

Requirements
Must have
• my name: Rosalind K Tarbury contact details: ros@quillsend.co.nz mobile - 021 583917 URL name: facebook.com/rosalindKtarbury - VordaLine
Photo of Me

```html
<!DOCTYPE html>
<html lang="en">
<head>
<meta charset="utf-8">
<title>VordaLine Business Card</title>
<link rel="stylesheet" href="https://fonts.googleapis.com/css2?family=Open+Sans:wght@400;700&family=Philosopher:wght@700&display=swap">
<style>
  :root {
    --bg: #dfe6ea;
    --teal-dark: #009e8e;
    --teal-mid: #52c3b7;
    --teal-light: #8ad6cc;
    --red: #d0434f;
    --white: #ffffff;
    --ink: #2c3a3a;
    --name: #0a9a8a;
    --photo-top: #3f6b34;
    --photo-bottom: #6f9a52;
  }
  * { box-sizing: border-box; margin: 0; padding: 0; }
  html, body { width: 1200px; height: 965px; overflow: hidden; }
  body { background: var(--bg); position: relative; font-family: "Open Sans", sans-serif; }

  .card {
    position: absolute;
    left: 284px;
    width: 634px;
    height: 362px;
    border-radius: 17px;
    overflow: hidden;
    background: var(--white);
  }
  .card--front { top: 103px; }
  .card--back { top: 525px; background: var(--teal-mid); }
  .card__shapes { position: absolute; inset: 0; width: 100%; height: 100%; }

  .brand {
    position: absolute;
    font-family: "Philosopher", sans-serif;
    font-weight: 700;
    color: var(--white);
    line-height: 1;
    white-space: nowrap;
  }
  .card--front .brand { right: 28px; bottom: 22px; font-size: 50px; }
  .card--back .brand { left: 0; right: 0; top: 128px; text-align: center; font-size: 78px; }

  .contact { position: absolute; left: 317px; top: 68px; }
  .contact__name { font-size: 20px; font-weight: 700; color: var(--name); margin-bottom: 8px; }
  .contact__line { display: flex; align-items: center; gap: 9px; font-size: 16px; color: var(--ink); height: 24px; }
  .contact__icon { width: 14px; height: 14px; flex: none; }
</style>
</head>
<body>

<section class="card card--front">
  <svg class="card__shapes" viewBox="0 0 528 302" preserveAspectRatio="none">
    <defs>
      <linearGradient id="photoTone" x1="0" y1="0" x2="0" y2="1">
        <stop offset="0" stop-color="var(--photo-top)"/>
        <stop offset="1" stop-color="var(--photo-bottom)"/>
      </linearGradient>
    </defs>
    <rect x="0" y="0" width="228" height="250" fill="url(#photoTone)" role="img" aria-label="Photo of the coach leaping in the air in front of a green hedge"/>
    <path d="M228 0 H234 V56 L250 68 L234 80 V230 H228 Z" fill="var(--red)"/>
    <path d="M0 250 Q 300 250 528 118 V302 H0 Z" fill="var(--teal-light)" opacity="0.85"/>
    <path d="M0 235 Q 90 285 270 268 Q 430 250 528 158 V302 H0 Z" fill="var(--red)"/>
    <path d="M0 278 Q 180 292 330 262 Q 450 236 528 170 V302 H0 Z" fill="var(--teal-dark)"/>
  </svg>

  <div class="contact">
    <p class="contact__name">Rosalind K Tarbury</p>
    <p class="contact__line">
      <svg class="contact__icon" viewBox="0 0 14 14"><rect x="3" y="0.5" width="8" height="13" rx="1.5" fill="none" stroke="var(--red)" stroke-width="1.5"/><rect x="5.5" y="10.5" width="3" height="1.2" fill="var(--red)"/></svg>
      021 583917
    </p>
    <p class="contact__line">
      <svg class="contact__icon" viewBox="0 0 14 14"><rect x="0.5" y="2.5" width="13" height="9" fill="var(--red)"/><path d="M0.5 2.5 L7 8 L13.5 2.5" fill="none" stroke="var(--white)" stroke-width="1.2"/></svg>
      ros@quillsend.co.nz
    </p>
    <p class="contact__line">
      <svg class="contact__icon" viewBox="0 0 14 14"><rect x="1" y="1" width="12" height="12" fill="var(--red)"/></svg>
      rosalindKtarbury
    </p>
  </div>

  <p class="brand">VordaLine</p>
</section>

<section class="card card--back">
  <svg class="card__shapes" viewBox="0 0 528 302" preserveAspectRatio="none">
    <path d="M0 240 Q 300 250 528 195 V302 H0 Z" fill="var(--teal-light)"/>
    <path d="M0 228 Q 60 262 250 262 Q 430 258 528 228 V302 H0 Z" fill="var(--red)"/>
    <path d="M0 262 Q 100 272 270 270 Q 430 266 528 238 V302 H0 Z" fill="var(--teal-dark)"/>
  </svg>
  <p class="brand">VordaLine</p>
</section>

</body>
</html>
```